Print on top the name of the company: (Or Similar)
Larkmoor Cleaning & Disinfecting
Because your standards aren't standard.

We adhere to ALL NVB guidelines for both residential and commercial cleaning.

Infection Control is our ultimate goal.

Instructions:
Opening a residential and commercial cleaning and disinfecting company in south Florida.

Targeting high-end residential clients, commercial and healthcare facilities, specializing in Ambulatory Care Guidelines. With a concentration and expertise in targeting Covid 19 and other transmissible pathogens.

UMRE trained.
Owned and operated by a licensed BSN Registered Nurse specially ​trained in Infection Control Prevention with over 25 years experience. Over two decades in Ambulatory Surgery Center Administration, Director of Nursing and Infection Control Prevention ad Consulting.

Looking to create a business flier that emphasizes Cleaning & Disinfection
along with the standard expectation for residential and Commercial cleaning services
Updates

Need extra days to review

Target Market(s)

Residential & Commercial

Font styles to use
Decorative

Requirements
Must have
• A checklist for cleaning services

```html
<!DOCTYPE html>
<html lang="en">
<head>
<meta charset="utf-8">
<title>Larkmoor Cleaning &amp; Disinfecting – Flyer</title>
<link rel="stylesheet" href="https://fonts.googleapis.com/css2?family=Barlow:wght@400;500;600;700;800;900&family=Barlow+Semi+Condensed:wght@700&family=Rubik:wght@800&display=swap">
<style>
  :root {
    --orange: #f7941d;
    --black: #050608;
    --charcoal: #3a3b3d;
    --mist: #e7e8ea;
    --white: #ffffff;
    --ink: #1b1b1d;
    --body-text: #2b2b2d;
    --divider: #555555;
    --backdrop: #9c9da1;
  }
  * { margin: 0; padding: 0; box-sizing: border-box; }
  html, body { width: 906px; height: 1200px; overflow: hidden; background: var(--backdrop); }
  .flyer {
    position: absolute; left: 29px; top: 0;
    width: 848px; height: 1200px;
    background: var(--white); overflow: hidden;
    font-family: "Barlow", sans-serif; color: var(--ink);
  }
  .flyer__shapes, .flyer__photo { position: absolute; left: 0; top: 0; }
  .flyer__mid-shade {
    position: absolute; left: 0; top: 350px; width: 848px; height: 448px;
    background: linear-gradient(90deg, var(--mist) 0%, var(--white) 32%);
  }
  .brand-name {
    position: absolute; left: 65px; top: 65px;
    font-weight: 900; font-size: 72px; line-height: 75px; letter-spacing: -0.5px;
    color: var(--black); text-transform: uppercase;
  }
  .brand-rule {
    position: absolute; left: 65px; top: 217px; width: 300px; height: 3px;
    background: linear-gradient(90deg, rgba(40,40,40,0.2), #2a2a2a 45%, rgba(40,40,40,0.1));
  }
  .tagline {
    position: absolute; left: 65px; top: 229px;
    font-weight: 600; font-size: 27px; line-height: 34px; color: var(--black);
  }
  .guideline-note {
    position: absolute; left: 0; width: 848px; top: 454px; text-align: center;
    font-weight: 600; font-size: 17.5px; line-height: 22px; color: var(--black);
  }
  .goal {
    position: absolute; left: 0; width: 848px; top: 482px; text-align: center;
    font-weight: 600; font-size: 35px; line-height: 42px; color: var(--orange); letter-spacing: 0.2px;
  }
  .info-col {
    position: absolute; top: 548px; height: 224px;
    display: flex; align-items: center; justify-content: center;
    text-align: center; font-size: 16.2px; line-height: 20.6px; color: var(--body-text);
  }
  .info-col--intro { left: 40px; width: 240px; }
  .info-col--focus { left: 288px; width: 226px; }
  .info-col--owner { left: 524px; width: 276px; }
  .service-panel {
    position: absolute; top: 798px; width: 424px; height: 259px; text-align: center;
    font-family: "Barlow Semi Condensed", sans-serif; font-weight: 700; color: var(--white);
  }
  .service-panel--commercial { left: 0; background: var(--black); }
  .service-panel--residential { left: 424px; background: var(--orange); }
  .service-panel__title {
    margin-top: 26px; font-family: "Barlow", sans-serif; font-weight: 800;
    font-size: 27px; line-height: 30px; letter-spacing: 0.3px;
  }
  .service-list { list-style: none; margin-top: 14px; font-size: 16px; line-height: 20.6px; }
  .contact-band {
    position: absolute; left: 0; top: 1057px; width: 848px; height: 143px;
    background: var(--mist); text-align: center; color: var(--black);
  }
  .contact-band__cta {
    position: absolute; left: 0; width: 100%; top: 32px;
    font-family: "Rubik", sans-serif; font-weight: 800; font-size: 25px; line-height: 30px; letter-spacing: -0.3px;
  }
  .contact-band__phone {
    position: absolute; left: 0; width: 100%; top: 62px;
    font-weight: 800; font-size: 49px; line-height: 56px; letter-spacing: -0.5px;
  }
</style>
</head>
<body>
  <main class="flyer">
    <div class="flyer__mid-shade"></div>

    <svg class="flyer__shapes" width="848" height="798" viewBox="0 0 848 798" aria-hidden="true">
      <polygon points="0,0 511,0 424,420 0,350" fill="var(--orange)"/>
      <polygon points="424,420 848,221 848,332" fill="var(--charcoal)"/>
      <line x1="283.5" y1="547" x2="283.5" y2="771" stroke="var(--divider)" stroke-width="1"/>
      <line x1="520.5" y1="547" x2="520.5" y2="771" stroke="var(--divider)" stroke-width="1"/>
    </svg>

    <svg class="flyer__photo" width="848" height="420" viewBox="0 0 848 420" role="img"
         aria-label="Photo of a cleaner in a blue uniform carrying a caddy of cleaning supplies by a door">
      <defs>
        <linearGradient id="photoTone" x1="0" y1="0" x2="1" y2="0">
          <stop offset="0" stop-color="#2b4fae"/>
          <stop offset="0.55" stop-color="#3658b4"/>
          <stop offset="0.8" stop-color="#8a8c88"/>
          <stop offset="1" stop-color="#c9c6bf"/>
        </linearGradient>
      </defs>
      <polygon points="511,0 848,0 848,221 424,420" fill="url(#photoTone)"/>
    </svg>

    <h1 class="brand-name">Larkmoor<br>Cleaning</h1>
    <div class="brand-rule"></div>
    <p class="tagline">Larkmoor Cleaning &amp;<br>Disinfecting Because your<br>standards aren't standard.</p>

    <p class="guideline-note">We adhere to ALL NVB guidelines for both residential and commercial cleaning.</p>
    <h2 class="goal">INFECTION CONTROL IS OUR ULTIMATE GOAL.</h2>

    <p class="info-col info-col--intro">INSTRUCTIONS:<br>Opening a residential and<br>commercial cleaning and<br>disinfecting company in<br>south Florida.</p>
    <p class="info-col info-col--focus">Targeting high-end<br>residential clients,<br>commercial and<br>healthcare facilities,<br>specializing in Ambulatory<br>Care Guidelines. With a<br>concentration and<br>expertise in targeting<br>Covid 19 and other<br>transmissible pathogens.</p>
    <p class="info-col info-col--owner">UMRE TRAINED.<br>Owned and operated by a<br>licensed BSN Registered Nurse<br>specially trained in Infection<br>Control Prevention with over 25<br>years experience. Over two<br>decades in Ambulatory Surgery<br>Center Administration, Director<br>of Nursing and Infection Control<br>Prevention ad Consulting.</p>

    <section class="service-panel service-panel--commercial">
      <h3 class="service-panel__title">COMMERCIAL</h3>
      <ul class="service-list">
        <li>janitorial</li>
        <li>Offices</li>
        <li>Floor maintenance</li>
        <li>Carpet cleaning</li>
        <li>Move-ins</li>
        <li>Move-outs</li>
        <li>Construction clean-ups</li>
        <li>Estate clean-outs</li>
      </ul>
    </section>

    <section class="service-panel service-panel--residential">
      <h3 class="service-panel__title">RESIDENTIAL</h3>
      <ul class="service-list">
        <li>House cleaning</li>
        <li>Before and after party</li>
        <li>Move-ins</li>
        <li>Move-outs</li>
        <li>Holiday cleaning</li>
        <li>Seasonal cleaning</li>
        <li>Carpet cleaning</li>
        <li>Deodorizing and sanitizing</li>
      </ul>
    </section>

    <footer class="contact-band">
      <p class="contact-band__cta">Call us to find out how you can save money this month!</p>
      <p class="contact-band__phone">(555) 010 24 68</p>
    </footer>
  </main>
</body>
</html>
```